Website Design for Harrowgate Aquacut - Specialised Waterjet Cutting Service Provider

Description:
We are seeking a talented and creative web designer to create a new, single-page scrolling website for our company, Harrowgate Aquacut. We specialise in providing waterjet cutting services, with over 15 years of experience in the industry and a strong focus on serving the film and TV sector. Our goal is to showcase our expertise, services, and dedication to delivering exceptional quality and timely project completion.
Design Requirements:
Use existing website as a template: Please use our current website (www.harrowgateaquacut.example) as a template for the new design. We would like the new website to maintain a similar structure and feel, but with a refreshed and modernised appearance.
Single-page scrolling website: Design a single-page scrolling website with clear, intuitive navigation for each section.
Professional and modern design: The website should have a clean, professional, and modern aesthetic that appeals to both film industry professionals and other potential clients seeking waterjet cutting services.
Responsive design: The website must be fully responsive and compatible with various devices, including desktop computers, laptops, tablets, and smartphones.
Colour scheme: We prefer a colour scheme that includes shades of blue, grey, and white. However, we are open to creative suggestions that align with our brand identity and industry.
Typography: The font choice should be clean, legible, and professional.
Imagery: The website should incorporate high-quality images showcasing our waterjet cutting services, machinery, and examples of completed projects.
Integration of plain review badge Reviews: The website design should incorporate a section or widget that displays our plain review badge Reviews, highlighting our customers' positive experiences and showcasing our commitment to quality service.
Contact Information: Instead of a contact form, please include our email address and telephone number on the site, accompanied by a friendly message encouraging visitors to get in touch with us for any inquiries.
Industries Served: While our primary focus is the film and TV industry, please highlight that we also cater to aerospace, motorsport, engineering projects, oil and gas, pharmaceutical, space, fusion energy, and EV projects. Also, mention that we have worked with several YouTubers.
Fastest Turnaround Time: Emphasise that we have the fastest turnaround time for waterjet cutting services in the south of the UK.
Friendly and Creative Team: Emphasise that we are a friendly team who enjoy working with creative individuals, fostering a collaborative and enjoyable working environment for all parties involved.
Proposed Website Sections:
Home
About Us
Services
Portfolio
Testimonials
Contact Us
Please provide initial design concepts for the single-page scrolling website, keeping in mind the similarity to our existing website. We look forward to reviewing your creative proposals and working with you to create a website that effectively represents our brand and appeals to our target audience while maintaining the essence of our current website.
Target Market(s)
Film Industry
Coding
Look and feel

```html
<!DOCTYPE html>
<html lang="en">
<head>
<meta charset="utf-8">
<title>Harrowgate Aquacut</title>
<link href="https://fonts.googleapis.com/css2?family=Nunito:wght@400;600;700&family=Raleway:wght@300;700;800&display=swap" rel="stylesheet">
<style>
:root{
  --blue:#1a6690;
  --blue-dark:#0f4f73;
  --orange:#f26a1e;
  --ink:#3d3d3d;
  --grey:#6b6b6b;
  --pale:#eef3f7;
  --footer:#333335;
  --white:#ffffff;
}
*{margin:0;padding:0;box-sizing:border-box}
html,body{width:1200px;height:4073px;overflow:hidden;background:var(--white)}
body{position:relative;font-family:"Nunito",sans-serif;color:var(--ink)}
.abs{position:absolute}

/* header */
.brand{left:111px;top:28px;display:flex;align-items:center;gap:10px;white-space:nowrap}
.brand-mark{width:20px;height:20px;background:var(--blue);flex:none}
.brand-name{font-family:"Raleway",sans-serif;font-weight:800;font-size:20px;color:var(--blue);letter-spacing:.5px;white-space:nowrap}
.follow{left:675px;top:44px;font-size:14px;color:var(--grey);display:flex;align-items:center;gap:8px}
.soc{width:22px;height:22px;border-radius:50%;background:var(--blue);display:inline-block}
.call{left:860px;top:44px;font-size:14px;color:var(--grey)}
.phone-top{left:925px;top:34px;font-size:25px;font-weight:700;color:var(--orange)}
.nav{left:0;top:93px;width:1200px;height:57px;background:var(--blue)}
.nav-item{position:absolute;top:0;transform:translateX(-50%);color:var(--white);font-weight:700;font-size:17px;line-height:57px;white-space:nowrap;text-shadow:0 1px 2px rgba(0,0,0,.3)}
.nav-sep{position:absolute;top:0;width:2px;height:57px;background:var(--blue-dark)}

/* hero */
.hero{left:0;top:150px;width:1200px;height:633px;
  clip-path:polygon(0 0,100% 0,100% 498px,1091px 633px,0 498px);
  background:linear-gradient(120deg,#c9d6e0 0%,#8ea5b8 30%,#4e6e88 55%,#2b4a63 75%,#9fb3c3 100%)}
.hero-title{left:0;width:1200px;top:330px;text-align:center;font-family:"Raleway",sans-serif;font-size:41px;color:var(--white)}
.hero-title b{font-weight:800}.hero-title span{font-weight:300}
.hero-sub{left:250px;width:700px;top:397px;text-align:center;font-size:19px;line-height:31px;color:var(--white)}
.btn{display:flex;align-items:center;justify-content:center;color:var(--white);font-weight:700;text-transform:uppercase;background:var(--orange);clip-path:polygon(0 0,100% 0,88% 100%,0 100%);white-space:nowrap}
.hero-btn{left:520px;top:487px;width:157px;height:49px;font-size:15px;padding-right:16px}

/* about */
.about-title{left:111px;top:838px;font-family:"Raleway",sans-serif;font-size:47px;color:var(--blue)}
.about-title b{font-weight:800}.about-title span{font-weight:300;color:#444}
.body-text{font-size:14px;line-height:25px;color:var(--grey);text-align:justify}
.about-left{left:111px;top:912px;width:472px}
.about-right{left:617px;top:844px;width:472px}
.read-btn{left:617px;top:1001px;width:158px;height:47px;font-size:15px;padding-right:16px}
.photo-cut1{left:103px;top:1088px;width:608px;height:367px;background:linear-gradient(135deg,#2f3c48,#8da4b8 45%,#dfe7ee 70%,#6f8aa0)}
.photo-cut2{left:601px;top:1213px;width:479px;height:360px;background:linear-gradient(160deg,#6d5c44 0%,#3e6fa8 35%,#6fb0e6 60%,#2d5f99 100%)}
.years{left:711px;top:1140px;width:176px;height:73px;background:var(--blue);color:var(--white);font-family:"Raleway",sans-serif;font-weight:800;font-size:25px;display:flex;align-items:center;justify-content:center}
.experience{left:927px;top:1161px;font-size:22px;font-weight:600;color:#333}
.frame-line{left:406px;top:1455px;width:196px;height:60px;border-left:4px solid var(--blue);border-bottom:4px solid var(--blue)}

/* materials */
.materials{left:0;top:1608px;width:1200px;height:651px;
  clip-path:polygon(0 132px,111px 0,100% 112px,100% 100%,0 100%);
  background:linear-gradient(110deg,#2f6a93 0%,#1b5f8a 40%,#13557f 100%)}
.mat-frame{left:111px;top:1747px;width:170px;height:170px;background:var(--white);clip-path:polygon(0 0,100% 0,80% 100%,0 100%)}
.mat-photo{left:145px;top:1782px;width:412px;height:409px;background:linear-gradient(135deg,#6f6a62,#a89f90 40%,#d9cfbf 60%,#5a544c)}
.mat-title{left:615px;top:1788px;font-family:"Raleway",sans-serif;font-weight:800;font-size:37px;color:var(--white)}
.mat-text{left:617px;width:472px;font-size:14.5px;line-height:24.7px;color:var(--white);text-align:justify}

/* portfolio */
.portfolio-bg{left:0;top:2259px;width:1200px;height:753px;background:var(--pale);
  clip-path:polygon(0 0,100% 0,100% 618px,1091px 753px,0 618px)}
.section-title{left:0;width:1200px;text-align:center;font-family:"Raleway",sans-serif;font-weight:800;font-size:44px;color:var(--blue)}
.slide-left{left:0;top:2455px;width:223px;height:359px;clip-path:polygon(0 0,100% 0,100% 100%,0 88%);background:linear-gradient(160deg,#0e2a33,#1f5a63 50%,#6fb7b3 75%,#142b30)}
.slide-main{left:300px;top:2455px;width:600px;height:359px;background:linear-gradient(180deg,#5d7a92,#a9bccb 45%,#c9d5de 70%,#7d92a3)}
.slide-caption{left:300px;top:2770px;width:600px;text-align:center;font-family:"Raleway",sans-serif;font-weight:700;font-size:21px;color:var(--white);text-shadow:0 1px 3px rgba(0,0,0,.5)}
.slide-right{left:977px;top:2455px;width:223px;height:359px;clip-path:polygon(0 0,100% 0,100% 88%,0 100%);background:linear-gradient(200deg,#3b2a26,#9d2a22 35%,#cfc7c2 60%,#efe9e4)}
.arrow{width:28px;height:40px}

/* testimonials */
.card{top:3170px;width:305px;height:359px;background:var(--white);box-shadow:0 2px 14px rgba(0,0,0,.12);padding:38px 25px 0}
.stars{color:var(--orange);font-size:13px;letter-spacing:2px}
.quote{margin-top:14px;font-size:13.5px;line-height:23.3px;color:var(--grey);text-align:justify}
.reviewer{position:absolute;left:25px;top:290px}
.reviewer-name{font-family:"Raleway",sans-serif;font-weight:700;font-size:20px;color:#333}
.reviewer-town{font-size:11px;color:#888}
.badge{position:absolute;right:25px;top:292px;width:100px;height:38px;border-radius:4px;background:#e8edf2}

/* footer */
.footer{left:0;top:3632px;width:1200px;height:441px;background:var(--footer);clip-path:polygon(0 138px,111px 0,100% 138px,100% 100%,0 100%)}
.foot-brand{left:111px;top:3862px;width:185px;height:67px;background:var(--white);display:flex;align-items:center;justify-content:center;gap:6px}
.foot-brand .brand-name{font-size:13px;letter-spacing:0}
.foot-brand .brand-mark{width:12px;height:12px}
.foot-h{top:3782px;font-weight:700;font-size:17px;color:var(--white);white-space:nowrap}
.foot-label{left:392px;font-size:12px;font-weight:700;color:var(--white)}
.foot-val{left:392px;font-size:12px;color:var(--orange);text-decoration:underline;white-space:nowrap}
.foot-addr{left:392px;top:3941px;font-size:12px;line-height:18px;color:var(--white)}
.foot-ico{left:358px;width:14px;height:14px}
.foot-links{left:672px;top:3826px;list-style:none;font-size:13px;line-height:26.8px;color:var(--white)}
.foot-note{left:841px;top:3826px;width:250px;font-size:12px;line-height:21px;color:var(--white)}
.foot-btn{left:841px;top:3908px;width:198px;height:43px;font-size:13px;background:var(--blue);padding-right:14px}
.foot-rule{left:111px;top:4011px;width:978px;height:1px;background:#777}
.copyright{left:111px;top:4030px;font-size:12px;color:var(--white)}
.foot-soc{top:4025px;width:28px;height:28px;border-radius:50%}
</style>
</head>
<body>

<!-- header -->
<div class="abs brand"><span class="brand-mark"></span><span class="brand-name">HARROWGATE AQUACUT</span></div>
<div class="abs follow">Follow us on <span class="soc"></span><span class="soc" style="margin-left:-6px"></span></div>
<div class="abs call">Call us</div>
<div class="abs phone-top">01632 960418</div>

<nav class="abs nav">
  <span class="nav-item" style="left:153px">HOME</span>
  <span class="nav-sep" style="left:225px"></span>
  <span class="nav-item" style="left:300px">ABOUT US</span>
  <span class="nav-sep" style="left:375px"></span>
  <span class="nav-item" style="left:463px">SERVICES</span>
  <span class="nav-sep" style="left:542px"></span>
  <span class="nav-item" style="left:631px">PORTFOLIO</span>
  <span class="nav-sep" style="left:723px"></span>
  <span class="nav-item" style="left:821px">TESTIMONIALS</span>
  <span class="nav-sep" style="left:917px"></span>
  <span class="nav-item" style="left:1017px">CONTACT US</span>
</nav>

<!-- hero -->
<div class="abs hero" role="img" aria-label="Waterjet cutting head spraying high-pressure water and abrasive"></div>
<h1 class="abs hero-title"><b>HARROWGATE</b> <span>AQUACUT</span></h1>
<p class="abs hero-sub">Providing A Profile Cutting Service of Virtually Any Material To Customers Specifications Using High-Pressure Water With Abrasive</p>
<a class="abs btn hero-btn">Contact Us</a>

<!-- about -->
<h2 class="abs about-title"><b>ABOUT</b> <span>US</span></h2>
<p class="abs body-text about-left">Harrowgate Aquacut has been providing a profile cutting service primarily to the film industry for over 15 years. We are used to working within tight timeframes with a fast turnaround for all aspects of Water Jet Profiling, Abrasive Steel Cutting and Foam-Water Jet Cutting.</p>
<p class="abs body-text about-right">By combining our technical expertise with Aqualine's latest dynamic head waterjet technology we are able to offer a Profiling Services which can be tailored to each individual client and completed within fine tolerances to precise specifications. We are happy to cut your material or where required we can source most materials to your requirement</p>
<a class="abs btn read-btn">Read More</a>

<div class="abs frame-line"></div>
<div class="abs photo-cut1" role="img" aria-label="Waterjet nozzle cutting a metal sheet over the water bed"></div>
<div class="abs years">15 YEARS</div>
<div class="abs experience">Experience</div>
<div class="abs photo-cut2" role="img" aria-label="Waterjet machine cutting a blue acrylic disc"></div>

<!-- materials -->
<div class="abs materials" role="img" aria-label="Blue-toned waterjet workshop background"></div>
<div class="abs mat-frame"></div>
<div class="abs mat-photo" role="img" aria-label="Operator guiding a cut metal part under a waterjet head"></div>
<h2 class="abs mat-title">MATERIALS</h2>
<p class="abs mat-text" style="top:1867px">Materials we can cut include, but are not limited to, all metals &amp; alloys, composites, solid surface, wood, glass, acrylics, resins , silicones, plastics, foams, carpet &amp; felts. We can also cut laminated dissimilar which can often be very hard to cut using conventional methods. We are always happy to test cut a sample of your material free of charge to demonstrate the quality of cut achievable.</p>
<p class="abs mat-text" style="top:2031px">Employing Aqualine's Low pressure vacuum assist we can pierce and cut brittle materials such as acrylic In addition, our adaptive-head technology with live tolerance tracking produces more accurate parts at significantly higher cutting speeds than parts cut with a conventional waterjet. If you are not sure whether waterjet cutting will fulfil your requirements give us a call.</p>

<!-- portfolio -->
<div class="abs portfolio-bg"></div>
<h2 class="abs section-title" style="top:2352px">PORTFOLIO</h2>
<div class="abs slide-left" role="img" aria-label="Teal-lit cutting heads in a machine"></div>
<div class="abs slide-main" role="img" aria-label="Waterjet head over a cutting table for an engineering project"></div>
<div class="abs slide-caption">ENGINEERING PROJECTS</div>
<div class="abs slide-right" role="img" aria-label="Red cutting disc throwing sparks"></div>
<svg class="abs arrow" style="left:106px;top:2614px" viewBox="0 0 28 40"><polyline points="20,6 8,20 20,34" fill="none" stroke="#fff" stroke-width="4"/></svg>
<svg class="abs arrow" style="left:1066px;top:2614px" viewBox="0 0 28 40"><polyline points="8,6 20,20 8,34" fill="none" stroke="#fff" stroke-width="4"/></svg>

<!-- testimonials -->
<h2 class="abs section-title" style="top:3068px">TESTIMONIALS</h2>
<div class="abs card" style="left:111px">
  <div class="stars">★★★★★</div>
  <p class="quote">"Lorem ipsum dolor sit amet, consectetur adipiscing elit, sed do eiusmod tempor incididunt ut labore et dolore magna aliq ua. Ut enim ad minim veniam, quis nost rud exercitation ullamco laboris nisi ut aliquip ex ea commodo consequat. Duis aute irure dolor in reprehenderit in volup tate velit esse cillum dolore eu fugiat nulla parhend siteiatur."</p>
  <div class="reviewer"><div class="reviewer-name">Sam Porter</div><div class="reviewer-town">Kingsmere</div></div>
  <div class="badge" role="img" aria-label="Review platform badge"></div>
</div>
<div class="abs card" style="left:447px">
  <div class="stars">★★★★★</div>
  <p class="quote">"Lorem ipsum dolor sit amet, consectetur adipiscing elit, sed do eiusmod tempor incididunt ut labore et dolore magna aliq ua. Ut enim ad minim veniam, quis nost rud exercitation ullamco laboris nisi ut aliquip ex ea commodo consequat. Duis aute irure dolor in reprehenderit in volup tate velit esse cillum dolore eu fugiat nulla parhend siteiatur."</p>
  <div class="reviewer"><div class="reviewer-name">Sam Porter</div><div class="reviewer-town">Kingsmere</div></div>
  <div class="badge" role="img" aria-label="Review platform badge"></div>
</div>
<div class="abs card" style="left:783px">
  <div class="stars">★★★★★</div>
  <p class="quote">"Lorem ipsum dolor sit amet, consectetur adipiscing elit, sed do eiusmod tempor incididunt ut labore et dolore magna aliq ua. Ut enim ad minim veniam, quis nost rud exercitation ullamco laboris nisi ut aliquip ex ea commodo consequat. Duis aute irure dolor in reprehenderit in volup tate velit esse cillum dolore eu fugiat nulla parhend siteiatur."</p>
  <div class="reviewer"><div class="reviewer-name">Sam Porter</div><div class="reviewer-town">Kingsmere</div></div>
  <div class="badge" role="img" aria-label="Review platform badge"></div>
</div>

<!-- footer -->
<div class="abs footer"></div>
<div class="abs foot-brand"><span class="brand-mark"></span><span class="brand-name">HARROWGATE AQUACUT</span></div>

<div class="abs foot-h" style="left:359px">CONTACT US</div>
<svg class="abs foot-ico" style="top:3826px" viewBox="0 0 14 14"><path d="M3 1l2.5 3-1.5 1.5a8 8 0 0 0 4.5 4.5L10 8.5l3 2.5-1.5 2C6 13 1 8 1 2.5z" fill="#999"/></svg>
<div class="abs foot-label" style="top:3825px">Phone</div>
<div class="abs foot-val" style="top:3845px">01632 960418</div>
<svg class="abs foot-ico" style="top:3874px" viewBox="0 0 14 14"><rect x="1" y="3" width="12" height="9" fill="#999"/><polyline points="1,3 7,8 13,3" fill="none" stroke="#333" stroke-width="1.2"/></svg>
<div class="abs foot-label" style="top:3872px">Email</div>
<div class="abs foot-val" style="top:3892px">hello@harrowgateaquacut.example</div>
<svg class="abs foot-ico" style="top:3923px" viewBox="0 0 14 14"><path d="M7 1a4 4 0 0 1 4 4c0 3-4 8-4 8S3 8 3 5a4 4 0 0 1 4-4z" fill="#999"/><circle cx="7" cy="5" r="1.5" fill="#333"/></svg>
<div class="abs foot-label" style="top:3921px">Location</div>
<div class="abs foot-addr">Unit 7, Riverside Works, Kiln Lane,<br>Marlow Trade Park, Harrowgate,<br>HG4 9ZX , UK</div>

<div class="abs foot-h" style="left:666px">COMPANY</div>
<ul class="abs foot-links"><li>Home</li><li>About Us</li><li>Services</li><li>Portfolio</li><li>Testimonials</li><li>Contact Us</li></ul>

<div class="abs foot-h" style="left:841px">STIL HAVE QUESTIOS?</div>
<p class="abs foot-note">Harrowgate Aquacut has been providing a profile cutting service primarily to the film industry for over 15 years.</p>
<a class="abs btn foot-btn">Contact Us Today</a>

<div class="abs foot-rule"></div>
<div class="abs copyright">© 2023 Comany name &nbsp;| All Rights Reserved</div>
<span class="abs foot-soc" style="left:1022px;background:#fff"></span>
<span class="abs foot-soc" style="left:1058px;background:var(--orange)"></span>

</body>
</html>
```